Flyer Design Project

I need a flyer designed for my new dog grooming business.
I have just ordered fridge magnet business cards and would like a flyer to send them out with, if you could create a flyer and put some ideas together using the information provided to help promote my business.
The business is called Tallowby Pawcare,
I groom small dogs.
I’d like to have on the flyer the services I offer,
One on one quality care for the customers pet,
Full dog grooms, clipper clips, scissor snips and full shaves,
Sanitary clips, nails clipped, DE shedding,
Various brushing styles and techniques,
All professional equipment and products used,
Medicated shampoos & groomers fluffana wash & colognes,
Hydro dog bath and heater blow dryer.
My profession also id like to have on the flyer:
(A certified pet hygienist & dog Groomer)
I’d like the Tallowby Pawcare logo with the purple paw prints in the writing on the flyer ( will upload pic of logo)
I’d also like the website displayed the email and the phone number all clearly on the flyer also thank you.
Website address: tallowbypawcare.com.au
Email address: info@tallowbypawcare.com.au
Phone number: 0412 580 264
When this flyer has finally been created & finalised, I will need to have sent to me all raw formats and fonts i.e. vector files to be able to provide my sign writer to make the grey in my logo foil instead of silver. Thankyou

regarding size of the flyer i would like the flyer to be size A5 (210mm x 148mm) thankyou.

also when adding dogs to the flyer try sick to the smaller breeds all the flyers look great so far

can i also please have the website,phone number and email writting big or bold on the flyer to stand out.
thankyou
Updates

the text medicated shampoos, groomers fluffana was & colones are now to be changed to

(medicated shampoo's, groomers fluffana & scented colones)

and one on one quality care for the customers pet changed to

(one on one quality care for your pet)

Target Market(s)

dog owners

Industry/Entity Type

Pet

Requirements
Should not have
• no pricings included or any special deals

```html
<!DOCTYPE html>
<html lang="en">
<head>
<meta charset="utf-8">
<title>Tallowby Pawcare – Flyer</title>
<link rel="stylesheet" href="https://fonts.googleapis.com/css2?family=Sniglet:wght@400;800&family=Tinos&display=swap">
<style>
  :root {
    --sky: #3f87c9;
    --sky-light: #5aa0dc;
    --navy: #0c0550;
    --white: #ffffff;
    --butter: #fbf28a;
    --photo-tan: #c89a62;
    --photo-blue: #7fa9d6;
  }
  * { margin: 0; padding: 0; box-sizing: border-box; }
  html, body { width: 800px; height: 1200px; overflow: hidden; background: var(--sky); }
  .flyer {
    position: relative;
    width: 800px;
    height: 1200px;
    overflow: hidden;
    background: var(--sky);
    font-family: "Tinos", "Times New Roman", serif;
    color: var(--white);
  }
  .photo-area {
    position: absolute;
    inset: 0;
    width: 800px;
    height: 1200px;
  }
  .title-band {
    position: absolute;
    left: 0;
    top: 24px;
    width: 800px;
    height: 152px;
    background: var(--navy);
    display: flex;
    align-items: center;
    justify-content: center;
  }
  .business-name {
    font-family: "Sniglet", "Arial Rounded MT Bold", sans-serif;
    font-weight: 800;
    font-size: 62px;
    letter-spacing: 1px;
    color: var(--white);
    padding-left: 20px;
  }
  .tagline {
    position: absolute;
    left: 68px;
    top: 212px;
    font-family: "Sniglet", "Arial Rounded MT Bold", sans-serif;
    font-size: 35px;
    color: var(--white);
    white-space: nowrap;
  }
  .credential {
    position: absolute;
    left: 30px;
    top: 300px;
    width: 450px;
    text-align: center;
    font-size: 29px;
    line-height: 40px;
  }
  .services-heading {
    position: absolute;
    left: 42px;
    top: 492px;
    font-family: "Sniglet", "Arial Rounded MT Bold", sans-serif;
    font-size: 32px;
    color: var(--butter);
  }
  .services-list {
    position: absolute;
    left: 73px;
    top: 566px;
    width: 540px;
    list-style: none;
    font-size: 25px;
    line-height: 36px;
  }
  .contact {
    position: absolute;
    left: 46px;
    top: 1036px;
    font-size: 23px;
    line-height: 31px;
  }
  .contact-intro { color: var(--white); margin-bottom: 9px; }
  .contact-line { color: var(--butter); }
</style>
</head>
<body>
<main class="flyer">
  <svg class="photo-area" viewBox="0 0 800 1200" role="img" aria-label="Photograph of a small tan and white dog sitting, smiling, against a blue sky">
    <defs>
      <linearGradient id="photoTone" x1="0" y1="0" x2="0" y2="1">
        <stop offset="0" stop-color="var(--photo-blue)"/>
        <stop offset="0.35" stop-color="var(--photo-tan)"/>
        <stop offset="0.75" stop-color="#d9c3a4"/>
        <stop offset="1" stop-color="var(--photo-blue)"/>
      </linearGradient>
    </defs>
    <path d="M725 0 C 560 190, 480 420, 500 640 C 520 880, 640 1090, 750 1200 L800 1200 L800 0 Z" fill="url(#photoTone)"/>
  </svg>

  <header class="title-band">
    <h1 class="business-name">Tallowby Pawcare</h1>
  </header>

  <p class="tagline">One on one quality care for your pet</p>

  <p class="credential">from a certified<br>pet hygienist &amp; Dog Groomer</p>

  <h2 class="services-heading">Our Services</h2>
  <ul class="services-list">
    <li>Full dog grooms, clipper clips, scissor snips and full shaves,</li>
    <li>Sanitary clips, nails clipped, DE shedding,</li>
    <li>Various brushing styles and techniques,</li>
    <li>All professional equipment and products used,</li>
    <li>Medicated shampoos &amp; groomers fluffana wash &amp; colognes,</li>
    <li>Hydro dog bath and heater blow dryer.</li>
  </ul>

  <section class="contact">
    <p class="contact-intro">Contact us on :-</p>
    <p class="contact-line">Website address: tallowbypawcare.com.au</p>
    <p class="contact-line">Email address: info@tallowbypawcare.com.au</p>
    <p class="contact-line">Phone number: 0412 580 264</p>
  </section>
</main>
</body>
</html>
```